依頼詳細
最近、全国高校用教科書を編集しています。この度、これに対応した『テキスト』を関連編集しています。全部で16 unitありますが、設問のパターンはほとんど同じものです。ですから、『unit1』を対象に、6ページの基本編集レイアウトの作成を依頼したいのです。よろしくお願いします。
記載項目
『unit1』の原稿は添付いたします。
希望イメージ
シンプル 複雑
単色 カラフル
暗い 明るい
日常 高級
遊び心 厳粛
未来的 伝統的
女性的 男性的
希望する色
納品ファイル
• 高解像度JPG (.jpg)
• イラストレーター形式 (.ai)
補足説明
■ 選んだ理由

全ページのバランスが最もとれており、見本ページにふさわしかったので、本提案を当選として選びました。

■ 提案者全員のお礼・コメント

お盆休みの中、たくさんの御提案をいただきまして、大変感謝しております。当社は出版社ですから、依頼事項が続きます。今後とも、よろしくお願い申し上げます。

```html
<!DOCTYPE html>
<html lang="ja">
<head>
<meta charset="utf-8">
<title>Unit 1 Henry, This Is Oliver</title>
<link href="https://fonts.googleapis.com/css2?family=Noto+Sans+JP:wght@400;500;700;900&display=swap" rel="stylesheet">
<style>
:root{
  --ink:#1a1a1a;
  --band:#6f6f6f;
  --band-light:#d9d9d9;
  --paper:#ffffff;
  --muted:#555555;
}
*{margin:0;padding:0;box-sizing:border-box}
html,body{width:848px;height:1200px;overflow:hidden;background:var(--paper)}
body{font-family:"Noto Sans JP",sans-serif;color:var(--ink);position:relative}
.page{position:absolute;inset:0}
.unit-header{position:absolute;left:28px;top:16px;width:792px;height:66px;background:var(--band);border:2px solid var(--ink)}
.unit-label{position:absolute;left:0;top:0;width:184px;height:62px;background:var(--ink);color:var(--paper);font-weight:900;font-size:34px;letter-spacing:2px;display:flex;align-items:center;justify-content:center;gap:22px}
.unit-title{position:absolute;left:212px;top:2px;color:var(--paper);font-weight:900;font-size:36px;line-height:42px}
.unit-source{position:absolute;left:212px;top:44px;color:var(--paper);font-size:13px;font-weight:500}
.skills-bar{position:absolute;left:28px;top:102px;width:792px;height:30px;background:linear-gradient(90deg,var(--band-light),#f4f4f4 70%,var(--paper));border-top:1px solid #999;border-bottom:1px solid #999;display:flex;align-items:center;padding-left:12px;font-weight:700;font-size:18px;gap:10px}
.skills-bar svg{flex:none}
.score-box{position:absolute;left:622px;top:105px;width:198px;height:36px;border:1.5px solid var(--ink);background:var(--paper)}
.score-box .tag{position:absolute;left:0;top:0;background:var(--ink);color:var(--paper);font-size:9px;padding:1px 5px}
.score-box svg{position:absolute;right:20px;top:4px}
.section-mark{position:absolute;left:34px;width:26px;height:26px;background:var(--ink);color:var(--paper);font-weight:700;font-size:18px;display:flex;align-items:center;justify-content:center}
.instruction{position:absolute;left:74px;font-size:15px;line-height:31px;width:720px}
.line{position:absolute;font-size:16px;white-space:pre}
.num{position:absolute;left:74px;font-size:16px}
.ab{position:absolute;left:128px;font-size:16px}
.word{position:absolute;font-size:16px;text-align:center}
.word u{text-decoration:underline;text-underline-offset:3px}
.dot{position:absolute;width:12px;height:12px;border-radius:50%;background:var(--ink)}
.tip{position:absolute;left:74px;top:978px;width:720px;font-size:15px;line-height:31px}
.tip .indent{padding-left:118px;display:block}
</style>
</head>
<body>
<div class="page">
  <header class="unit-header">
    <div class="unit-label"><span>UNIT</span><span>1</span></div>
    <h1 class="unit-title">Henry, This Is Oliver</h1>
    <p class="unit-source">Oliver Small</p>
  </header>

  <div class="skills-bar">
    <svg width="18" height="18" viewBox="0 0 18 18"><circle cx="9" cy="9" r="8" fill="#333"/><circle cx="9" cy="9" r="4" fill="#aaa"/></svg>
    Listening Skills
  </div>
  <div class="score-box"><span class="tag">得点</span>
    <svg width="28" height="28" viewBox="0 0 28 28"><line x1="24" y1="2" x2="4" y2="26" stroke="#1a1a1a" stroke-width="1.5"/></svg>
  </div>

  <div class="section-mark" style="top:160px">A</div>
  <p class="instruction" style="top:157px">CD を聴き、空所を埋めなさい。強勢アクセントに注意しながら、会話練習をしましょう。</p>

  <span class="num" style="top:218px">（1）</span><span class="ab" style="top:218px">a.　( How ) are things with you?</span>
  <span class="ab" style="top:252px">b.　I'm getting ( along ) very well, thank you.</span>
  <span class="num" style="top:297px">（2）</span><span class="ab" style="top:297px">a.　( What ) do you ( do )?</span>
  <span class="ab" style="top:331px">b.　I'm a ( high )( school )( teacher ).</span>
  <span class="num" style="top:376px">（3）</span><span class="ab" style="top:376px">a.　( Where ) do you ( live )?</span>
  <span class="ab" style="top:410px">b.　I live ( in ) Minami-ku.</span>
  <span class="num" style="top:453px">（4）</span><span class="ab" style="top:453px">a.　( What ) is your ( favorite ) subject?</span>
  <span class="ab" style="top:487px">b.　I like Japanese and ( mathematics ) best.</span>

  <div class="section-mark" style="top:550px">B</div>
  <p class="instruction" style="top:547px">CD を聴き、次の英文をリピートしてみましょう。その際、強弱のリズムに気をつけましょう。下線部要素（主語名詞、本動詞、目的語名詞）は強勢アクセント●が付与され、強く発音されます。</p>

  <span class="num" style="top:680px">（5）</span><span class="ab" style="top:680px">a.</span>
  <span class="word" style="left:232px;top:680px"><u>Dogs</u></span><span class="dot" style="left:243px;top:712px"></span>
  <span class="word" style="left:418px;top:680px"><u>bite</u></span><span class="dot" style="left:426px;top:712px"></span>
  <span class="word" style="left:604px;top:680px"><u>bones</u></span><span class="dot" style="left:619px;top:712px"></span>

  <span class="ab" style="top:780px">b.</span>
  <span class="word" style="left:198px;top:780px">The<u>dogs</u></span><span class="dot" style="left:243px;top:812px"></span>
  <span class="word" style="left:342px;top:780px">will</span>
  <span class="word" style="left:418px;top:780px"><u>bite</u></span><span class="dot" style="left:426px;top:812px"></span>
  <span class="word" style="left:570px;top:780px">the<u>bones</u></span><span class="dot" style="left:619px;top:812px"></span>

  <span class="ab" style="top:876px">c.</span>
  <span class="word" style="left:198px;top:876px">The<u>dogs</u></span><span class="dot" style="left:243px;top:908px"></span>
  <span class="word" style="left:330px;top:876px">will have<u>bitten</u></span><span class="dot" style="left:426px;top:908px"></span>
  <span class="word" style="left:570px;top:876px">the<u>bones</u></span><span class="dot" style="left:619px;top:908px"></span>

  <p class="tip">Listening Tip: 内容語である名詞、動詞、形容詞には、強勢アクセントが付与され、一方、<span class="indent">機能語である代名詞、助動詞、冠詞などには、強勢アクセントが付与されず、弱く発音される場合が多い。</span></p>
</div>
</body>
</html>
```